Product Box packaging design for CBD Candy Company

We need a complete product box design (dieline template included in zip file) for an online-based CBD Candy product. The Company, Holloway Sweets, will be marketing to a mature online audience through a well-established influencer, who focuses on ASMR. We will provide detailed information as to what will be needed on each side of the product box, but need help with the aesthetic aspect of the packaging. We would like to focus on soothing/calming colors and pull in an organic/ nature aspect. The company is based in Tennessee. We will provide a color palette that will mimic the colors of the website as well. Please refer to the zip-file for all specifications.

Target Market(s)

Online subsribers to an established Influencer

Industry/Entity Type

CBD candy industry

Requirements
Must have
• Please follow the dieline template for sizing. The box is 3.5"x3.5"X1.75"
Nice to have
• We want classic, calming, with a nature/rustic and simple feel if possible

```html
<!DOCTYPE html>
<html lang="en">
<head>
<meta charset="utf-8">
<title>Holloway Sweets – CBD Caramels Box</title>
<link rel="stylesheet" href="https://fonts.googleapis.com/css2?family=Oswald:wght@400;600;700&family=Montserrat:wght@400;600&display=swap">
<style>
  :root{
    --bg:#e3e5e6;
    --green:#4a8e70;
    --khaki:#b8bd6a;
    --white:#ffffff;
    --fold:#3f7c61;
  }
  *{box-sizing:border-box;margin:0;padding:0}
  html,body{width:1200px;height:900px;overflow:hidden;background:var(--bg)}
  .dieline{position:relative;width:1200px;height:900px}
  .panel{position:absolute;background:var(--green);color:var(--white);
    font-family:'Montserrat',sans-serif;outline:1px dashed var(--fold);overflow:hidden}
  .panel-top{left:380px;top:100px;width:440px;height:440px}
  .panel-left{left:160px;top:100px;width:220px;height:440px;padding:34px 22px}
  .panel-right{left:820px;top:100px;width:220px;height:440px;padding:34px 22px}
  .panel-front{left:380px;top:540px;width:440px;height:220px;padding:22px 26px}

  .brand{font-family:'Oswald',sans-serif;font-weight:600;color:var(--white);
    letter-spacing:.12em;text-transform:uppercase;display:flex;align-items:center;gap:8px}
  .brand-dot{width:14px;height:14px;border-radius:50%;border:2px solid var(--white);flex:none}
  .panel-top .brand{position:absolute;right:28px;top:26px;font-size:13px}

  .title{font-family:'Oswald',sans-serif;font-weight:700;text-transform:uppercase;line-height:.9;display:flex;flex-direction:column}
  .title-row{display:flex;align-items:flex-end;gap:.12em}
  .title-cbd{color:var(--khaki)}
  .title-sub{color:var(--white);font-size:.28em;line-height:1;padding-bottom:.14em}
  .title-main{color:var(--white);letter-spacing:.01em}
  .panel-top .title{position:absolute;left:56px;top:78px;font-size:74px}
  .panel-left .title{font-size:37px}

  .dose{position:absolute;left:56px;top:250px;display:flex;align-items:center;gap:14px}
  .dose-tag{background:var(--khaki);color:var(--white);font-family:'Oswald',sans-serif;
    font-weight:700;font-size:22px;padding:4px 12px;text-transform:uppercase}
  .dose-note{font-size:12px;line-height:1.3;text-transform:uppercase}
  .dose-note strong{text-transform:none;font-weight:600}
  .rule{height:2px;background:var(--khaki)}
  .panel-top .rule{position:absolute;left:56px;top:304px;width:330px}

  .pack-info{position:absolute;left:56px;bottom:40px;display:flex;align-items:center;gap:16px}
  .count{width:54px;height:54px;border:3px solid var(--white);border-radius:8px;display:flex;
    flex-direction:column;align-items:center;justify-content:center;font-family:'Oswald',sans-serif}
  .count b{font-size:24px;line-height:1}
  .count span{font-size:8px;text-transform:uppercase;letter-spacing:.05em}
  .net{font-family:'Oswald',sans-serif;font-size:15px;line-height:1.25}
  .net b{font-weight:700}
  .net span{font-family:'Montserrat',sans-serif;font-size:13px}

  .warning-box{border:2px solid var(--white);margin:20px 0 12px;padding:6px;text-align:center;
    font-weight:600;font-size:13px}
  .small{font-size:9.5px;line-height:1.45}
  .panel-right .brand{font-size:12px;margin-bottom:26px}
  .panel-right .small + .small{margin-top:14px}

  .front-text{width:220px}
  .ingredients-head{font-family:'Oswald',sans-serif;font-weight:600;color:var(--khaki);
    text-transform:uppercase;font-size:14px;margin-bottom:2px}
  .panel-front .rule{margin:10px 0 8px;width:200px}
  .maker{font-size:10px;line-height:1.3}
  .maker b{font-family:'Oswald',sans-serif;font-weight:600}
  .front-mark{position:absolute;right:26px;top:50%;transform:translateY(-50%);
    display:flex;align-items:center;gap:10px}
  .front-mark .brand-dot{width:46px;height:46px;border:4px solid var(--khaki)}
  .front-mark .name{font-family:'Oswald',sans-serif;font-weight:600;color:var(--khaki);
    font-size:22px;letter-spacing:.1em;text-transform:uppercase;line-height:1.05}
</style>
</head>
<body>
<main class="dieline">

  <section class="panel panel-left">
    <h2 class="title">
      <span class="title-row"><span class="title-cbd">CBD</span><span class="title-sub">Infused<br>Sea Salted</span></span>
      <span class="title-main">Caramels</span>
    </h2>
    <div class="warning-box">Warning:</div>
    <p class="small">This product is not intended for use by any persons under the age of 21. Keep out of reach of children. Do not consume this product if you are pregnant or nursing. Do not operate heavy machinery while using. This product contains full spectrum hemp which may yield a drowsy effect, please use responsibly.</p>
  </section>

  <section class="panel panel-top">
    <div class="brand"><span class="brand-dot"></span>Holloway Sweets</div>
    <h1 class="title">
      <span class="title-row"><span class="title-cbd">CBD</span><span class="title-sub">Infused<br>Sea Salted</span></span>
      <span class="title-main">Caramels</span>
    </h1>
    <div class="dose">
      <span class="dose-tag">35 mg CBD</span>
      <span class="dose-note">Per caramel<br><strong>420 mg per Box</strong></span>
    </div>
    <div class="rule"></div>
    <div class="pack-info">
      <div class="count"><b>12</b><span>Per box</span></div>
      <p class="net"><b>Net Wt 2.52 OZ</b><br><span>(72 gm)</span></p>
      <svg width="34" height="34" viewBox="0 0 34 34" aria-hidden="true"><rect x="7" y="7" width="20" height="20" transform="rotate(45 17 17)" fill="none" stroke="#ffffff" stroke-width="2"/></svg>
    </div>
  </section>

  <section class="panel panel-right">
    <div class="brand"><span class="brand-dot"></span>Holloway Sweets</div>
    <p class="small">It is recommended to consume no more than 2 caramels per day. Please allow sufficient time between consumption of candies, typically one hour is recommended.</p>
    <p class="small">This product has not been evaluated by the Food and Drug Administration and is not intended to diagnose, treat, cure or prevent any disease. This product is legal under the 2018 U.S. Farm Bill and contains less than 0.3% THC by dry weight basis.</p>
  </section>

  <section class="panel panel-front">
    <div class="front-text">
      <p class="ingredients-head">Ingredients:</p>
      <p class="small">sugar, water, corn syrup, heavy cream, butter, vinegar, CO2 extracted full spectrum hemp distillate, sea salt</p>
      <div class="rule"></div>
      <p class="maker"><b>Handcrafted x Small Batch</b><br>Holloway Sweets, LLC</p>
      <p class="small" style="margin-top:6px">Visit www.hollowaysweets.com for more information on the wonders of CBD and the high quality lab tested CBD and other ingredients utilized in our caramels.</p>
    </div>
    <div class="front-mark">
      <span class="brand-dot"></span>
      <span class="name">Holloway<br>Sweets</span>
    </div>
  </section>

</main>
</body>
</html>
```